Flyer Design

I will be hosting an event at Penrith's amber lantern. Here is a link to their page http://www.theamberlantern.com.au/events-and-workshops/whats-on-penrith/. I have attached the details of my course from their website below. I hope this is of some valuable assistance.

Florist and lover of all things gorgeous, Molly Hartwell from Molly Hartwell Flowers will be running this beautiful and fun workshop. Come along to learn how to make your very own floral crown. All you need to bring are some closed in shoes, an apron and an open mind ready for creativity!

Teens & adults welcome

Date 1: Saturday 11 April 2015
Time 1: 11:00-2:00pm

Date 2: Thursday 23 April 2015
Time 2: 6:00-9:00pm

Cost: $90 per person (includes materials provided – see list below)
Place: The Amber Lantern, Unit 3, 27 Baxter Lane Penrith
RSVP: Molly via email mollyhartwellflowers@fernmail.example or phone 0431 795 206

Materials provided:
• Florist scissors
• Parafilm
• Wire
• Flowers
• light snacks & refreshments

```html
<!DOCTYPE html>
<html lang="en">
<head>
<meta charset="utf-8">
<title>Floral Crowns Workshop</title>
<link href="https://fonts.googleapis.com/css2?family=Yesteryear&family=PT+Sans:ital,wght@0,400;0,700;1,700&family=PT+Sans+Narrow&display=swap" rel="stylesheet">
<style>
  :root {
    --pink-light: #f8bdd3;
    --pink-mid: #f3a9c4;
    --pink-band: #eb93b0;
    --pink-ring: #d86f9c;
    --berry: #b3275b;
    --lime: #c7de57;
    --lime-light: #d6ea82;
    --ink: #1d1d1b;
    --white: #ffffff;
    --dash: #b9b9b9;
    --bullet: #e4709b;
  }
  html, body { margin: 0; padding: 0; overflow: hidden; }
  body { width: 1200px; height: 851px; }
  .flyer {
    position: relative;
    width: 1200px;
    height: 851px;
    overflow: hidden;
    background: linear-gradient(90deg, var(--pink-mid) 0%, #ecc3b0 22%, #d6dd83 38%, var(--lime) 55%, var(--lime) 100%);
    font-family: "PT Sans", sans-serif;
    color: var(--ink);
  }
  .top-panel {
    position: absolute; left: 0; top: 0; width: 1200px; height: 193px;
    background: linear-gradient(100deg, #f4a8c4 0%, var(--pink-light) 45%, var(--pink-light) 100%);
  }
  .top-panel .blossom-backdrop {
    position: absolute; left: 430px; top: 0; width: 380px; height: 193px;
    background: radial-gradient(ellipse at 40% 30%, rgba(240,130,165,0.55), rgba(248,189,211,0) 70%);
  }
  .address-band {
    position: absolute; left: 0; top: 193px; width: 1200px; height: 49px;
    background: var(--pink-band);
    color: var(--white);
    font-weight: 700; font-size: 23px;
    display: flex; align-items: center; justify-content: center;
    padding-left: 430px; box-sizing: border-box;
  }
  .frame {
    position: absolute; left: 8px; top: 8px; right: 8px; bottom: 18px;
    border: 2px dashed var(--dash);
    pointer-events: none;
  }
  .portrait {
    position: absolute; left: -55px; top: -70px; width: 528px; height: 528px;
    border-radius: 50%;
    border: 7px solid var(--pink-ring);
    background: radial-gradient(circle at 55% 55%, #8a6150 0%, #b48c7a 30%, #ebe5e3 62%, #f4f2f2 100%);
    box-sizing: border-box;
  }
  .title {
    position: absolute; left: 450px; top: 28px; width: 730px;
    text-align: center;
    font-family: "Yesteryear", cursive;
    font-size: 70px; line-height: 1;
    margin: 0; font-weight: 400;
  }
  .sessions {
    position: absolute; left: 450px; top: 116px; width: 730px;
    text-align: center; font-weight: 700; font-size: 22px; line-height: 32px;
    margin: 0;
  }
  .intro {
    position: absolute; left: 470px; top: 258px; width: 660px;
    text-align: center; font-family: "PT Sans Narrow", sans-serif;
    font-size: 21px; line-height: 29px; margin: 0;
  }
  .host-photo {
    position: absolute; left: 426px; top: 402px; width: 746px; height: 343px;
    background: var(--lime-light); padding: 7px; box-sizing: border-box;
  }
  .host-photo .fill {
    width: 100%; height: 100%;
    background: linear-gradient(90deg, #c9c2b8 0%, #e8e1d8 35%, #d8cfc8 65%, #c7bfb8 100%);
  }
  .pricing {
    position: absolute; left: 45px; top: 490px; width: 375px;
    text-align: center; color: var(--berry); font-weight: 700;
    font-size: 25px; line-height: 34px; margin: 0; letter-spacing: 0.5px;
  }
  .materials {
    position: absolute; left: 55px; top: 570px; margin: 0;
  }
  .materials h2 { margin: 0 0 2px; font-size: 19px; font-weight: 700; }
  .materials ul { list-style: none; margin: 0; padding: 0; }
  .materials li {
    font-size: 23px; font-weight: 700; line-height: 28px;
    display: flex; align-items: center; gap: 8px;
  }
  .materials li::before {
    content: ""; width: 17px; height: 17px; border-radius: 50%;
    background: var(--bullet); flex: none;
  }
  .rsvp {
    position: absolute; left: 0; top: 756px; width: 1200px;
    text-align: center; font-weight: 700; font-style: italic;
    margin: 0;
  }
  .rsvp .line { display: block; font-size: 24px; line-height: 28px; }
  .rsvp .phone {
    display: inline-flex; align-items: center; gap: 10px;
    font-size: 38px; line-height: 46px; margin-left: -100px;
  }
  .rsvp .phone svg { width: 28px; height: 28px; }
</style>
</head>
<body>
<main class="flyer">
  <div class="top-panel"><div class="blossom-backdrop" role="img" aria-label="Soft pink blossom photo backdrop"></div></div>
  <div class="address-band">The Amber Lantern, Unit 3, 27 Baxter Lane Penrith</div>

  <div class="portrait" role="img" aria-label="Photo of a model wearing a floral crown of roses"></div>

  <h1 class="title">Floral Crowns Workshop</h1>
  <p class="sessions">Saturday 11 April 2015 &middot; 11:00-2:00pm<br>Thursday 23 April 2015 &middot; 6:00-9:00pm</p>

  <p class="intro">Florist and lover of all things gorgeous, Molly Hartwell from Molly Hartwell Flowers will be running this beautiful and fun workshop. Come along to learn how to make your very own floral crown. All you need to bring are some closed in shoes, an apron and an open mind ready for creativity!</p>

  <div class="host-photo"><div class="fill" role="img" aria-label="Photo of the florist host in her flower studio"></div></div>

  <p class="pricing">Cost: $90 per person<br>Teens &amp; adults welcome</p>

  <section class="materials">
    <h2>Materials provided:</h2>
    <ul>
      <li>Florist scissors</li>
      <li>Parafilm</li>
      <li>Wire</li>
      <li>Flowers</li>
      <li>light snacks &amp; refreshments</li>
    </ul>
  </section>

  <p class="rsvp">
    <span class="line">RSVP to Molly via email mollyhartwellflowers@fernmail.example or call</span>
    <span class="phone">
      <svg viewBox="0 0 26 26" aria-hidden="true"><circle cx="13" cy="13" r="11.5" fill="none" stroke="#1d1d1b" stroke-width="2"/><path d="M9 7c-1.5 1-1.8 3-.8 5.5 1.2 3 3.5 5.6 6 6.6 1.6.6 2.8.3 3.6-.6l-2-2.2-1.6.8c-1.4-.8-2.6-2.3-3.2-3.8l1.3-1.2L10.8 7z" fill="#1d1d1b"/></svg>
      0431.795.206
    </span>
  </p>

  <div class="frame"></div>
</main>
</body>
</html>
```